Anzeigengestaltung für Online-Handel mit Edelmetallen
Zielgruppe
Online Handel mit Edelmetallen wie Gold und Silberbarren und Münzen.
Sowie der Ankauf von Gold per Postankauf
Aufgabenstellung
Ich möchte in verschiedenen Tageszeitungen in Deutschland Werbung schalten . Kleine Anzeigen etwas kleiner als Visitenkarten Größe wegen den Kosten.
Logo
Ihr Onlineshop für Edelmetalle
Vergleichen sie unsere Preis
Goldbarren / Falkenthaler
Shop.Wertkontorlo.de

```html
<!DOCTYPE html>
<html lang="de">
<head>
<meta charset="utf-8">
<title>Anzeige – Onlineshop für Edelmetalle</title>
<link rel="stylesheet" href="https://fonts.googleapis.com/css2?family=Bebas+Neue&family=Marcellus&family=Poppins:wght@400&family=Yeseva+One&display=swap">
<style>
  :root {
    --page-bg: #f0eff0;
    --ad-bg: #373739;
    --gold: #cfa04c;
    --gold-light: #f2cf5c;
    --gold-deep: #a86f12;
    --white: #ffffff;
  }
  * { margin: 0; padding: 0; box-sizing: border-box; }
  html, body {
    width: 1200px;
    height: 1200px;
    overflow: hidden;
    background: var(--page-bg);
  }
  .ad {
    position: absolute;
    left: 0;
    top: 92px;
    width: 1200px;
    height: 1016px;
    background: var(--ad-bg);
    overflow: hidden;
  }
  .accent-circle {
    position: absolute;
    left: -199px;
    top: -250px;
    width: 594px;
    height: 594px;
    border-radius: 50%;
    background: var(--gold);
  }
  .headline {
    position: absolute;
    left: 68px;
    top: 68px;
    font-family: "Yeseva One", serif;
    font-size: 72px;
    line-height: 99px;
    color: var(--white);
    white-space: nowrap;
  }
  .tagline {
    position: absolute;
    left: 78px;
    top: 476px;
    font-family: "Bebas Neue", sans-serif;
    font-size: 84px;
    line-height: 91px;
    color: var(--white);
    letter-spacing: 1px;
  }
  .product-photo {
    position: absolute;
    left: 484px;
    top: 124px;
    width: 700px;
    height: 594px;
  }
  .shop-link {
    position: absolute;
    left: 62px;
    top: 851px;
    width: 645px;
    height: 90px;
  }
  .shop-link svg { position: absolute; inset: 0; }
  .shop-link span {
    position: absolute;
    inset: 0;
    display: flex;
    align-items: center;
    justify-content: center;
    font-family: "Poppins", sans-serif;
    font-size: 39px;
    color: var(--white);
  }
  .brand-name {
    position: absolute;
    left: 762px;
    top: 900px;
    width: 394px;
    text-align: center;
    font-family: "Marcellus", serif;
    font-size: 37px;
    color: var(--white);
    white-space: nowrap;
  }
</style>
</head>
<body>
  <main class="ad">
    <div class="accent-circle"></div>

    <h1 class="headline">Ihr Onlineshop<br>für Edelmetalle</h1>

    <svg class="product-photo" role="img" aria-label="Foto: Stapel glänzender Goldbarren" viewBox="0 0 700 594">
      <defs>
        <radialGradient id="goldGlow" cx="50%" cy="52%" r="55%">
          <stop offset="0%" stop-color="var(--gold-light)"/>
          <stop offset="55%" stop-color="#d9a326"/>
          <stop offset="85%" stop-color="var(--gold-deep)" stop-opacity="0.55"/>
          <stop offset="100%" stop-color="var(--ad-bg)" stop-opacity="0"/>
        </radialGradient>
      </defs>
      <rect width="700" height="594" fill="url(#goldGlow)"/>
    </svg>

    <p class="tagline">Vergleichen<br>Sie unsere<br>Preis!</p>

    <a class="shop-link">
      <svg viewBox="0 0 645 90" aria-hidden="true">
        <polygon points="22,3 642,3 642,66 618,87 3,87 3,24" fill="none" stroke="var(--gold)" stroke-width="4"/>
      </svg>
      <span>Shop.Wertkontorlo.de</span>
    </a>

    <div class="brand-name">Wertkontor-Lo.de</div>
  </main>
</body>
</html>
```